Multiple bag designs for poultry pellets

Terravane require a set of (x6) new bag designs for our 25kg poultry pellets. The bags must have 'made in the UK' and '100% organic' on the front of the design. An example of the current bag label is uploaded. A sketch of the requirements is also uploaded. Each design will require a different colour to make differentiation between bags. The final design must have space similar to the original for product information (i.e. the product specification). The bag brand should be Grovita - KB45

The front design should either utilise prominent cultural landmarks (UK & Ireland) as line drawings (e.g. Old Hesk etc). or utilisation of the following crops as either pictures or drawings:

Durian Fruit
Dragon fruit
Coffee
Rice
Banana
Sugar cane

Pictures could also depict Vietnam Agri landscapes

Target Market(s)

Organic farmers in Asia

Industry/Entity Type

Organic fertilisers

Font styles to use
Serif

Colors

Designer to choose colors to be used in the design.

Requirements
Must have
• 6 designs, based on the same theme (i.e colour, picture or pattern), must include 'made in uk' and '100% organic'
Nice to have
• A nod to poultry, i.e. chicken or the fact these are pellets (picture or line drawing)

```html
<!DOCTYPE html>
<html lang="en">
<head>
<meta charset="utf-8">
<title>Grovita - KB45 Poultry Pellets Bag</title>
<link rel="stylesheet" href="https://fonts.googleapis.com/css2?family=Oswald:wght@400;500;600&family=Open+Sans:wght@400;600&display=swap">
<style>
  :root {
    --bg: #efefef;
    --white: #ffffff;
    --yellow: #f4b83a;
    --yellow-light: #f8cf5f;
    --yellow-pale: #f6e27a;
    --green: #6aab35;
    --green-dark: #4f8f27;
    --brown: #3a2a1f;
    --ink: #2a211b;
    --orange: #e8732c;
    --cream: #fbf3dc;
    --badge-ring: #c9df9f;
    --grey-text: #6b6b6b;
  }
  * { margin: 0; padding: 0; box-sizing: border-box; }
  html, body { width: 1200px; height: 815px; overflow: hidden; background: var(--bg); }
  body { position: relative; font-family: "Open Sans", sans-serif; color: var(--ink); }

  .panel { position: absolute; top: 58px; height: 700px; background: var(--white); overflow: hidden; box-shadow: 0 2px 10px rgba(0,0,0,.08); }
  .panel-top { position: absolute; left: 0; top: 0; width: 100%; height: 86px; background: linear-gradient(180deg, var(--yellow) 0%, var(--yellow-light) 100%); }

  /* front */
  .front { left: 390px; width: 420px; }
  .product-title { position: absolute; left: 0; top: 18px; width: 100%; text-align: center; font-family: "Oswald", sans-serif; font-weight: 600; font-size: 44px; letter-spacing: 1px; color: var(--ink); line-height: 1; }
  .crop-art { position: absolute; left: 26px; top: 118px; width: 160px; height: 150px; border-radius: 40% 50% 45% 55%; background: linear-gradient(135deg, #f3f0e4 0%, #d9e66a 55%, #b8cf3a 100%); }
  .badge { position: absolute; left: 256px; top: 128px; width: 146px; height: 146px; }
  .landscape { position: absolute; left: 0; top: 300px; width: 100%; height: 170px; background: linear-gradient(180deg, #e9eef0 0%, #b9c2b8 25%, #8f9f4e 50%, #b6a23c 75%, #8ea437 100%); }
  .wave { position: absolute; left: 0; top: 400px; width: 420px; height: 300px; }
  .brand { position: absolute; left: 26px; top: 596px; }
  .brand-name { font-family: "Oswald", sans-serif; font-weight: 600; font-size: 32px; line-height: 1; color: var(--brown); letter-spacing: 1px; }
  .brand-tag { font-size: 8px; letter-spacing: 2px; color: var(--brown); margin-top: 3px; }
  .weight { font-family: "Oswald", sans-serif; font-weight: 600; font-size: 20px; color: var(--ink); margin-top: 6px; }
  .origin { position: absolute; right: 22px; bottom: 30px; display: flex; align-items: center; gap: 8px; font-family: "Oswald", sans-serif; font-weight: 500; font-size: 19px; color: var(--ink); }
  .flag { width: 30px; height: 18px; }

  /* sides */
  .side { width: 220px; }
  .side-left { left: 110px; }
  .side-right { left: 870px; }
  .vertical { position: absolute; writing-mode: vertical-rl; transform: rotate(180deg); font-family: "Oswald", sans-serif; line-height: 1; }
  .product-type { top: 110px; }
  .product-type .line { display: block; font-weight: 500; font-size: 36px; color: var(--green); }
  .product-type .line-dark { font-size: 26px; color: var(--ink); margin-left: 6px; }
  .side-brand { top: 340px; }
  .side-brand .brand-name { font-size: 48px; }
  .side-brand .brand-tag { font-family: "Open Sans", sans-serif; font-size: 9px; letter-spacing: 2px; color: var(--green-dark); margin-left: 4px; }
  .side-weight { position: absolute; bottom: 36px; font-family: "Oswald", sans-serif; font-weight: 600; font-size: 26px; color: var(--ink); }

  .side-left .product-type { left: 104px; }
  .side-left .side-brand { left: 104px; }
  .side-left .side-weight { left: 104px; }
  .side-right .product-type { left: 22px; }
  .side-right .side-brand { left: 22px; }
  .side-right .side-weight { left: 22px; }

  .analysis { position: absolute; left: 12px; top: 340px; height: 250px; writing-mode: vertical-rl; transform: rotate(180deg); border: 1px solid var(--green); border-radius: 4px; padding: 6px 4px; font-size: 6.5px; color: var(--grey-text); line-height: 1.6; }
  .analysis .row { border-left: 1px solid #d9e8c8; padding-left: 2px; white-space: nowrap; }
  .analysis .head { font-weight: 600; color: var(--green-dark); }

  .info { position: absolute; left: 134px; top: 110px; width: 76px; font-size: 6.5px; line-height: 1.45; color: var(--grey-text); }
  .info p { margin-bottom: 10px; }
  .info .nutrient { display: flex; align-items: center; gap: 3px; margin-bottom: 4px; }
  .info .dot { width: 6px; height: 6px; border-radius: 50%; background: var(--ink); flex: none; }
</style>
</head>
<body>

  <section class="panel side side-left">
    <div class="panel-top"></div>
    <div class="analysis">
      <div class="row head">Typical analysis</div>
      <div class="row">Organic matter 70%</div>
      <div class="row">Nitrogen 4%</div>
      <div class="row">Phosphate 3%</div>
      <div class="row">Potash 2.5%</div>
      <div class="row">Calcium 8%</div>
      <div class="row">Moisture 12%</div>
    </div>
    <div class="vertical product-type">
      <span class="line">POULTRY</span>
      <span class="line">PELLETS</span>
      <span class="line line-dark">FERTILIZER</span>
    </div>
    <div class="vertical side-brand">
      <div class="brand-name">TERRAVANE</div>
      <div class="brand-tag">NATURAL FERTILISER</div>
    </div>
    <div class="side-weight">25KG</div>
  </section>

  <section class="panel front">
    <div class="panel-top"><h1 class="product-title">GROVITA - KB45</h1></div>
    <div class="crop-art" role="img" aria-label="Line and colour drawing of a banana bunch with leaves"></div>
    <svg class="badge" viewBox="0 0 146 146" aria-label="100% organic badge">
      <circle cx="73" cy="66" r="62" fill="var(--badge-ring)"/>
      <circle cx="73" cy="66" r="54" fill="var(--white)"/>
      <circle cx="73" cy="66" r="46" fill="var(--cream)"/>
      <circle cx="73" cy="58" r="26" fill="#e0a35a" role="img" aria-label="Illustration of a hen"/>
      <path d="M2 94 L16 86 L130 86 L144 94 L130 102 L144 112 L16 112 L2 102 L16 94 Z" fill="#c95a1f"/>
      <rect x="12" y="82" width="122" height="26" rx="2" fill="var(--orange)"/>
      <text x="73" y="101" text-anchor="middle" font-family="Oswald, sans-serif" font-weight="600" font-size="17" fill="#ffffff">100% ORGANIC</text>
    </svg>
    <div class="landscape" role="img" aria-label="Photograph of terraced rice fields below misty mountains"></div>
    <svg class="wave" viewBox="0 0 420 300" preserveAspectRatio="none" aria-hidden="true">
      <defs>
        <linearGradient id="sand" x1="0" y1="0" x2="0" y2="1">
          <stop offset="0" stop-color="#f6c54c"/>
          <stop offset="1" stop-color="#f3b23a"/>
        </linearGradient>
      </defs>
      <path d="M0 110 C140 60 280 150 420 80 L420 300 L0 300 Z" fill="url(#sand)"/>
      <path d="M0 92 C140 40 280 130 420 60 L420 84 C280 150 140 70 0 118 Z" fill="var(--yellow-pale)"/>
      <path d="M0 50 C130 10 270 110 420 20 L420 66 C280 132 140 52 0 100 Z" fill="var(--green)"/>
    </svg>
    <div class="brand">
      <div class="brand-name">TERRAVANE</div>
      <div class="brand-tag">NATURAL FERTILISER</div>
      <div class="weight">25KG</div>
    </div>
    <div class="origin">
      <span>MADE IN THE UK</span>
      <svg class="flag" viewBox="0 0 30 18" aria-label="UK flag">
        <rect width="30" height="18" fill="#1f3f8f"/>
        <path d="M0 0 L30 18 M30 0 L0 18" stroke="#fff" stroke-width="3.6"/>
        <path d="M0 0 L30 18 M30 0 L0 18" stroke="#c8202f" stroke-width="1.2"/>
        <path d="M15 0 V18 M0 9 H30" stroke="#fff" stroke-width="6"/>
        <path d="M15 0 V18 M0 9 H30" stroke="#c8202f" stroke-width="3.4"/>
      </svg>
    </div>
  </section>

  <section class="panel side side-right">
    <div class="panel-top"></div>
    <div class="vertical product-type">
      <span class="line">POULTRY</span>
      <span class="line">PELLETS</span>
      <span class="line line-dark">FERTILIZER</span>
    </div>
    <div class="vertical side-brand">
      <div class="brand-name">TERRAVANE</div>
      <div class="brand-tag">NATURAL FERTILISER</div>
    </div>
    <div class="info">
      <p>Slow release pellets feed soil life and boost crop yield.</p>
      <p>Apply 150g per square metre before planting.</p>
      <p>Store dry and sealed after use.</p>
      <div class="nutrient"><span class="dot"></span>Nitrogen 4%</div>
      <div class="nutrient"><span class="dot"></span>Phosphate 3%</div>
      <div class="nutrient"><span class="dot"></span>Potash 2.5%</div>
    </div>
    <div class="side-weight">25KG</div>
  </section>

</body>
</html>
```